Business Card for premium dental clinic

We are a premium dental clinic based in Brasov, Romania with more than 15 year on the market, providing quality dental treatment made by a team of more specialized dentists, working with modern equipment as a solution to beautiful and healthy teeth.

Our current logo for the clinic use 2 square with colors black and gold - dr Merinca - studio, using family fonts Bodoni, Myriad Pro and Segoe Print.
Depending on the printing we used some gold CMYK background or gold foil picture background or a gold gradient.
We want a business card:
- eye catching business card
- distinguished business card
- premium design
- to keep the color scheme of black and gold
- to attract the customers to spent time reading the information
- modern concept

```html
<!DOCTYPE html>
<html lang="en">
<head>
<meta charset="utf-8">
<title>Merinca · Business Card</title>
<link rel="stylesheet" href="https://fonts.googleapis.com/css2?family=Open+Sans:wght@400;700&display=swap">
<style>
  :root {
    --ink: #000000;
    --paper: #ffffff;
    --gold: #f2b824;
    --backdrop: #e4e0da;
    --text-light: #f4f4f4;
  }
  * { box-sizing: border-box; margin: 0; padding: 0; }
  html, body { width: 1189px; height: 1200px; overflow: hidden; }
  body {
    position: relative;
    background: var(--backdrop);
    font-family: "Open Sans", Arial, sans-serif;
  }
  .card {
    position: absolute;
    left: 169px;
    width: 852px;
    height: 485px;
    border-radius: 34px;
    overflow: hidden;
    box-shadow: 0 6px 18px rgba(0,0,0,0.25);
    background: var(--ink);
  }
  .card--front { top: 112px; }
  .card--back { top: 641px; }
  .card__white-half {
    position: absolute; left: 0; top: 0; bottom: 0; width: 426px;
    background: var(--paper);
  }

  .brand-name {
    position: absolute;
    transform: translate(-50%, -50%);
    font-weight: 400;
    white-space: nowrap;
    letter-spacing: 1px;
  }
  .card--front .brand-name { left: 426px; top: 242px; font-size: 40px; color: var(--gold); }
  .card--back .brand-name { left: 213px; top: 243px; font-size: 36px; color: var(--ink); }

  .contact {
    position: absolute; left: 486px; top: 128px;
    color: var(--text-light);
  }
  .contact__name { font-size: 28px; font-weight: 700; line-height: 32px; color: var(--paper); }
  .contact__role { font-size: 20px; line-height: 24px; color: var(--gold); }
  .contact__address { margin-top: 18px; font-size: 19px; line-height: 28px; }
  .contact__list { list-style: none; margin-top: 8px; }
  .contact__item {
    display: flex; align-items: center; gap: 10px;
    font-size: 19px; line-height: 31px;
  }
  .contact__icon { width: 22px; height: 22px; flex: none; margin-left: -1px; }
</style>
</head>
<body>

<section class="card card--front" aria-label="Card front">
  <p class="brand-name">Merinca</p>
</section>

<section class="card card--back" aria-label="Card back">
  <div class="card__white-half"></div>
  <p class="brand-name">Merinca</p>

  <div class="contact">
    <p class="contact__name">Ioana Barbu</p>
    <p class="contact__role">Manager</p>
    <p class="contact__address">PO BOX 48, Lunga street<br>5th district Brasov</p>
    <ul class="contact__list">
      <li class="contact__item">
        <svg class="contact__icon" viewBox="0 0 22 22" aria-hidden="true">
          <circle cx="11" cy="11" r="11" fill="var(--gold)"/>
          <path d="M8 5.5 l2 3 -1.3 1.2 c0.6 1.4 1.6 2.5 3 3.2 l1.2 -1.3 3 2 -1 2 c-4.6 0.4 -9 -4 -8.8 -8.7z" fill="var(--ink)"/>
        </svg>
        <span>(040) 268 5512</span>
      </li>
      <li class="contact__item">
        <svg class="contact__icon" viewBox="0 0 22 22" aria-hidden="true">
          <circle cx="11" cy="11" r="11" fill="var(--gold)"/>
          <rect x="5.5" y="7" width="11" height="8" fill="none" stroke="var(--ink)" stroke-width="1.3"/>
          <path d="M5.5 7 L11 11.5 L16.5 7" fill="none" stroke="var(--ink)" stroke-width="1.3"/>
        </svg>
        <span>hello@merincastudio.com</span>
      </li>
      <li class="contact__item">
        <svg class="contact__icon" viewBox="0 0 22 22" aria-hidden="true">
          <circle cx="11" cy="11" r="11" fill="var(--gold)"/>
          <g fill="none" stroke="var(--ink)" stroke-width="1.2">
            <circle cx="11" cy="11" r="6"/>
            <ellipse cx="11" cy="11" rx="2.6" ry="6"/>
            <line x1="5" y1="11" x2="17" y2="11"/>
          </g>
        </svg>
        <span>www.merincastudio.com</span>
      </li>
    </ul>
  </div>
</section>

</body>
</html>
```